Web Design (Coded) and Project - Finance Company

Corvale Lending Group is a mortgage broker company based in Sydney Australia and provides lending solutions for individuals and businesses.

Our target market is anyone with the financial means to get a loan.

I am looking for a website design in this contest. The site needs to be able to be viewed on a portable device such as Tabra, Fonix, etc.

I have the logo design and files which need to be used. I also have the NLBC logo which will need to be in the footer of each page.

The website needs to represent a big finance company with integrity and knowledge.

The website will need to be uploaded to Hostwillow.example.au as they are the hosting provider. I will also need the ability to make changes to the text and pictures in the future and upload the revisions. I need the website ready to go and ready to be uploaded onto Host Willow.

The website will consist of 6 pages in total There are 4 main pages that will be viewed and then 2 with Privacy and Internal Dispute Resolution which are only accessed through links. These will be as follows:

Home
I would prefer to have a fresh bright and professional looking home page given that most mortgage broker websites look the same with the menu buttons at the top.

Services
Details the loan types that we handle and some text for each one.

About Us
I have the text for this.

Contact Us
Form to have the following inputs:
• Surname
• First Name
• Suburb
• State
• Phone number
• Mobile number
• Email address
• Preferred contact
o Phone
o Mobile
o Email
• Reason for Enquiry
o First home buyer
o Refinance
o Investment Property
o Commercial lending
o Personal loan
o Other
• Comments

Privacy
This page will only be accessed from a link at the bottom of each page. I have the wording that I will provide.

Dispute Resolution Policy
This page will only be accessed from a link on the Contact Us page. I have the wording that I will provide.
Updates

The designs that are coming through so far are generally looking the same generic website layout. I am looking for the home page to be something different with more of a wow factor and something different to the standard page link menu accross the top of the screen. The content should be fairly minimal given that I am a new business there will be limited text for each page. I am happy to increase the budget if required as I appreciate there will be more work involved.

Reason: I am extending the deadline as the design so far are good but fairly generic and template style home pages. For the home page I am looking for something a little more striking with a visual impact.

I have increased the payment by $200 to encourage more designs. Designs need to be relevant to the business, the number of pages and content. Several designs have come through looking good but just look like a standard template with my logo added, but the content does not match the business.

The brief stated that I am looking for the home page to be something different with more of a wow factor and something different to the standard page link menu accross the top of the screen. All of the designs have come through with the navigation bar along the top and a generic layout. I have attached a couple of idea's. Obviously these do not relate to the finance and mortgage industry but you can see the sort of style that gives the site a wow factor. The other pages can be more generic, but the first page is the attention grabber. You can also see the Fonix view that I am after. These are just templates from Host Willow that I could use to build the site, I just don't have the time or creative flair. Please submit more designs. Thanks for your work to date, Rob.

Hi. Could you please submit designs based on brief and the two screen shots attached. Mobile device view should work as per screen shots. Thanks, Rob

Reason: Still looking for designs to meet the brief provided.

Industry/Entity Type

Financial

Requirements
Must have
• Colour palette to be as supplied. I will post this shortly.
Should not have
• No cheesy smiley faces
No handshaking
No money pictures
No pictures of stones
No picture of people in an office looking at things
No lime green or purple in colour
Would prefer not to have a picture of the Quayline Span or Tidewater Hall

```html
<!DOCTYPE html>
<html lang="en">
<head>
<meta charset="utf-8">
<title>Corvale Lending Group — Mobile Home</title>
<link rel="stylesheet" href="https://fonts.googleapis.com/css2?family=Cinzel:wght@600&family=Tenor+Sans&family=Arimo:wght@400;700&display=swap">
<style>
  :root {
    --navy: #0d2f66;
    --navy-deep: #0a2450;
    --sky: #1ea0d8;
    --sky-light: #5cc3ea;
    --ink: #22324a;
    --grey-text: #8a8f96;
    --panel: #efefef;
    --btn-top: #f7f7f7;
    --btn-bottom: #c9c9c9;
    --field-line: #c9c9c9;
    --page-bg: #eef1f4;
    --white: #ffffff;
  }
  * { box-sizing: border-box; margin: 0; padding: 0; }
  html, body { width: 1118px; height: 1200px; overflow: hidden; }
  body { background: var(--page-bg); font-family: "Arimo", Arial, sans-serif; }

  .site {
    position: absolute; left: 227px; top: 34px;
    width: 664px; height: 1132px; overflow: hidden;
    background: var(--white);
  }
  .top-strip { height: 18px; background: var(--navy-deep); }

  .site-header {
    height: 152px; display: flex; justify-content: space-between; align-items: center;
    padding: 0 20px 0 16px; border-bottom: 5px solid var(--sky);
  }
  .brand { display: flex; align-items: center; gap: 22px; }
  .brand-mark { width: 112px; height: 112px; border-radius: 50%; background: var(--sky); }
  .brand-name {
    font-family: "Arimo", Arial, sans-serif; font-weight: 700; color: var(--ink);
    font-size: 30px; line-height: 31px; letter-spacing: 0.5px; text-transform: uppercase;
    padding-left: 18px; border-left: 2px solid #d5d8dc;
  }
  .call-box { text-align: right; align-self: flex-start; margin-top: 28px; }
  .call-label { color: var(--sky); font-size: 22px; }
  .call-number { display: flex; align-items: center; justify-content: flex-end; gap: 10px;
    color: var(--navy); font-weight: 700; font-size: 28px; margin-top: 2px; }
  .call-number svg { width: 26px; height: 26px; }

  .hero {
    position: relative; height: 264px;
    background: linear-gradient(100deg, #7fa7c9 0%, #2b4f7a 30%, #0f1f3d 60%, #1b3a6a 85%, #2c5b8f 100%);
  }
  .badge { position: absolute; right: 20px; bottom: 14px; width: 106px; height: 48px;
    background: var(--white); border: 3px solid #1c7fb4; border-radius: 3px; }

  .tagline {
    height: 48px; display: flex; align-items: center; justify-content: center;
    background: linear-gradient(90deg, var(--sky) 0%, var(--sky-light) 55%, var(--sky) 100%);
    font-family: "Cinzel", serif; font-weight: 600; font-size: 27px; color: var(--white);
    letter-spacing: 1px;
  }

  .main-nav { padding: 26px 22px 24px; border-bottom: 40px solid var(--panel); }
  .nav-item {
    height: 92px; margin-bottom: 3px; padding: 0 26px;
    display: flex; align-items: center; justify-content: space-between;
    background: linear-gradient(180deg, var(--btn-top), var(--btn-bottom));
    font-family: "Tenor Sans", sans-serif; font-size: 37px; color: var(--navy);
    text-transform: uppercase;
  }
  .nav-item svg { width: 26px; height: 44px; }

  .enquiry { padding: 0 4px; }
  .enquiry-title {
    height: 66px; background: var(--navy); color: var(--white);
    font-family: "Cinzel", serif; font-weight: 600; font-size: 32px;
    display: flex; align-items: center; padding-left: 22px; letter-spacing: 1px;
  }
  .field-row { display: flex; gap: 14px; margin-top: 16px; }
  .field { flex: 1; height: 48px; border: 2px solid var(--field-line); padding-left: 8px;
    display: flex; align-items: center; justify-content: space-between;
    color: var(--grey-text); font-size: 24px; }
  .field-select span.arrow { width: 30px; height: 100%; border-left: 2px solid var(--field-line);
    background: #e6e6e6; }
</style>
</head>
<body>
  <div class="site">
    <div class="top-strip"></div>

    <header class="site-header">
      <div class="brand">
        <div class="brand-mark"></div>
        <div class="brand-name">Corvale<br>Lending<br>Group</div>
      </div>
      <div class="call-box">
        <div class="call-label">call us today on</div>
        <div class="call-number">
          <svg viewBox="0 0 24 24"><rect width="24" height="24" rx="4" fill="#1ea0d8"/><path d="M8 5c1 0 2 3 2 4s-1 1-1 2 3 4 4 4 1-1 2-1 4 1 4 2-1 3-3 3C10 19 5 14 5 8c0-2 2-3 3-3z" fill="#fff"/></svg>
          1300 555 018
        </div>
      </div>
    </header>

    <section class="hero" role="img" aria-label="Photo of a businessman beside a night view of a lit harbour bridge and city skyline">
      <div class="badge"></div>
    </section>

    <div class="tagline">Providing you the right solution</div>

    <nav class="main-nav">
      <div class="nav-item">Home<svg viewBox="0 0 26 44"><path d="M5 4l16 18L5 40" fill="none" stroke="#1b6fa3" stroke-width="5"/></svg></div>
      <div class="nav-item">About Us<svg viewBox="0 0 26 44"><path d="M5 4l16 18L5 40" fill="none" stroke="#1b6fa3" stroke-width="5"/></svg></div>
      <div class="nav-item">Services<svg viewBox="0 0 26 44"><path d="M5 4l16 18L5 40" fill="none" stroke="#1b6fa3" stroke-width="5"/></svg></div>
      <div class="nav-item">Contact Us<svg viewBox="0 0 26 44"><path d="M5 4l16 18L5 40" fill="none" stroke="#1b6fa3" stroke-width="5"/></svg></div>
    </nav>

    <section class="enquiry">
      <h2 class="enquiry-title">Quick Enquiry</h2>
      <div class="field-row">
        <div class="field">First Name</div>
        <div class="field">Surname</div>
      </div>
      <div class="field-row">
        <div class="field field-select">State<span class="arrow"></span></div>
        <div class="field">Suburb</div>
      </div>
    </section>
  </div>
</body>
</html>
```